New Business Card Design Project

Hi there

Could you please make a design that is soft and appealing to people who would purchase gemstones, buy healing jewellery, seek counselling, may seek energy healing and/or learn English. Essentially I'm looking for something with a soft human design. Please incorporate the logo and select font that can be easily read and softer images in the background - but not too busy. I would like it double sided as well.

Optional: Elements could include gemstones, feathers, plants and images that are happy and calming.

Target Market(s)

People into alternative health, those from non-English speaking backgrounds, businesses

Contact Information for Business Card

Lena Whitford
Mobile: 0418 265 093, Facebook and Instagram Logos,
ABN: 61 472 185 034 (Australian Business Number - small at the bottom)

Requirements
Must have
• My project must have:
- Meadow Thread logo
- Symbols that represent the 4 main services: 1. Gemstones/jewellery, 2. counselling, 3. meditation/energy healing, 4. education
Nice to have
• Clear and easy to read.

```html
<!DOCTYPE html>
<html lang="en">
<head>
<meta charset="utf-8">
<title>Meadow Thread – Business Card</title>
<link href="https://fonts.googleapis.com/css2?family=Marcellus&family=Philosopher:wght@700&family=Arimo&family=Roboto+Condensed&display=swap" rel="stylesheet">
<style>
  :root {
    --backdrop: #2b2b2b;
    --paper: #e9e9e8;
    --teal: #13998a;
    --teal-soft: #3a9d90;
    --teal-deep: #2a8a7d;
    --leaf: #4f9a3a;
    --leaf-light: #7cb95c;
    --ink: #1d1d1d;
    --white: #f2f2f0;
  }
  * { margin: 0; padding: 0; box-sizing: border-box; }
  html, body { width: 1200px; height: 896px; overflow: hidden; background: var(--backdrop); }
  .stage { position: relative; width: 1200px; height: 896px; }

  .card {
    position: absolute;
    left: 357px;
    width: 486px;
    height: 278px;
    overflow: hidden;
  }
  .card--front { top: 160px; background: var(--paper); }
  .card--back { top: 469px; background: var(--teal-soft); }

  /* front */
  .brand { position: absolute; left: 44px; top: 34px; width: 136px; text-align: center; }
  .brand__dot {
    width: 44px; height: 44px; margin: 0 auto 6px;
    border: 2px solid var(--teal); border-radius: 50%;
  }
  .brand__name {
    font-family: "Marcellus", serif;
    font-size: 20px; line-height: 21px; letter-spacing: 1px;
    color: var(--leaf); text-transform: uppercase;
  }

  .details { position: absolute; left: 44px; top: 149px; font-family: "Arimo", sans-serif; color: var(--ink); }
  .details__abn { font-size: 11px; margin-bottom: 7px; }
  .details__list { list-style: none; }
  .details__item { display: flex; align-items: center; font-size: 11px; height: 14px; }
  .details__icon { width: 9px; height: 9px; margin-right: 8px; flex: none; }

  .services {
    position: absolute; left: 326px; top: 37px;
    display: grid; grid-template-columns: 54px 54px; gap: 9px 8px;
  }
  .service {
    width: 54px; height: 65px; border-radius: 4px;
    background: var(--teal);
    display: flex; flex-direction: column; align-items: center; justify-content: flex-end;
    padding-bottom: 6px;
    box-shadow: 0 1px 2px rgba(0,0,0,.2);
  }
  .service__icon { width: 28px; height: 28px; margin-bottom: 5px; }
  .service__label { font-family: "Roboto Condensed", sans-serif; font-size: 10px; color: var(--white); }

  .swoosh { position: absolute; left: 0; bottom: 0; width: 486px; height: 278px; }
  .holder {
    position: absolute; right: 27px; bottom: 14px;
    font-family: "Philosopher", sans-serif; font-weight: 700;
    font-size: 22px; color: var(--white);
  }

  /* back */
  .back__photo {
    position: absolute; inset: 0;
    background: linear-gradient(160deg, #46a496 0%, #3a9d90 45%, #2f9083 100%);
  }
  .back__brand { position: absolute; left: 0; right: 0; top: 68px; text-align: center; }
  .back__dot {
    width: 72px; height: 72px; margin: 0 auto 14px;
    border: 2px solid var(--white); border-radius: 50%;
  }
  .back__name {
    font-family: "Marcellus", serif;
    font-size: 28px; line-height: 30px; letter-spacing: 2px;
    color: var(--white); text-transform: uppercase;
  }
</style>
</head>
<body>
<main class="stage">

  <section class="card card--front">
    <div class="brand">
      <div class="brand__dot"></div>
      <p class="brand__name">Meadow<br>Thread</p>
    </div>

    <div class="details">
      <p class="details__abn">ABN: 61 472 185 034</p>
      <ul class="details__list">
        <li class="details__item">
          <svg class="details__icon" viewBox="0 0 10 10"><rect x="2.5" y="0.5" width="5" height="9" rx="1" fill="none" stroke="#4f9a3a" stroke-width="1.2"/></svg>
          0418 265 093
        </li>
        <li class="details__item">
          <svg class="details__icon" viewBox="0 0 10 10"><circle cx="5" cy="5" r="4.5" fill="#4f9a3a"/></svg>
          /MeadowThread
        </li>
        <li class="details__item">
          <svg class="details__icon" viewBox="0 0 10 10"><circle cx="5" cy="5" r="4.5" fill="#4f9a3a"/></svg>
          @MeadowThread
        </li>
        <li class="details__item">
          <svg class="details__icon" viewBox="0 0 10 10"><rect x="0.5" y="2" width="9" height="6" fill="#4f9a3a"/><path d="M0.5 2 L5 5.5 L9.5 2" fill="none" stroke="#e9e9e8" stroke-width="0.8"/></svg>
          info@MeadowThread.com
        </li>
      </ul>
    </div>

    <div class="services">
      <div class="service">
        <svg class="service__icon" viewBox="0 0 28 28" fill="none" stroke="#f2f2f0" stroke-width="1.3" stroke-linejoin="round">
          <path d="M7 10 L10 6 H18 L21 10 L14 22 Z"/><path d="M7 10 H21 M10 6 L12 10 L14 22 L16 10 L18 6"/>
        </svg>
        <span class="service__label">Jewellery</span>
      </div>
      <div class="service">
        <svg class="service__icon" viewBox="0 0 28 28" fill="none" stroke="#f2f2f0" stroke-width="1.4" stroke-linejoin="round">
          <path d="M14 22 C6 16 4 12 5 9 C6 5 11 5 14 9 C17 5 22 5 23 9 C24 12 22 16 14 22 Z"/>
        </svg>
        <span class="service__label">Counselling</span>
      </div>
      <div class="service">
        <svg class="service__icon" viewBox="0 0 28 28" fill="none" stroke="#f2f2f0" stroke-width="1.4">
          <circle cx="14" cy="14" r="8"/><circle cx="14" cy="14" r="2.5" fill="#f2f2f0"/>
        </svg>
        <span class="service__label">Meditation</span>
      </div>
      <div class="service">
        <svg class="service__icon" viewBox="0 0 28 28">
          <path d="M2 11 L14 6 L26 11 L14 16 Z" fill="#f2f2f0"/>
          <path d="M7 13.5 V18 C10 20.5 18 20.5 21 18 V13.5 L14 16.5 Z" fill="#f2f2f0"/>
          <path d="M24 12 V18" stroke="#f2f2f0" stroke-width="1.2"/>
        </svg>
        <span class="service__label">Education</span>
      </div>
    </div>

    <svg class="swoosh" viewBox="0 0 486 278" aria-hidden="true">
      <defs>
        <linearGradient id="leafBand" x1="0" y1="0" x2="1" y2="0">
          <stop offset="0" stop-color="#3f8a30"/>
          <stop offset="0.5" stop-color="#6aad4a"/>
          <stop offset="1" stop-color="#4f9a3a"/>
        </linearGradient>
      </defs>
      <path d="M0 258 L467 201 L70 278 L0 278 Z" fill="url(#leafBand)"/>
      <path d="M84 278 L486 204 L486 278 Z" fill="#13998a"/>
    </svg>
    <p class="holder">Lena Whitford</p>
  </section>

  <section class="card card--back">
    <div class="back__photo" role="img" aria-label="Soft photo of gemstones, crystals, leaves and a feather under a teal tint"></div>
    <div class="back__brand">
      <div class="back__dot"></div>
      <p class="back__name">Meadow<br>Thread</p>
    </div>
  </section>

</main>
</body>
</html>
```